Revamp PowerPoint deck to match our new website's visual identity and effectively tell our story

Revamp PowerPoint Deck to Match New Corporate Website Theme @ https://velrisdemo4.xq-stage.net/.
(Note: The content on the new theme is placeholder text. The current live website is www.tovalinfo.net )

Key Request: Slide Master SHOULD NOT include any specific contents. It should contain only essential elements such master layout, the logo, header, footer, and any repeating text elements and it should be limited to a maximum of 5 pages.

We need to redesign our existing PowerPoint deck to align with the visual identity of our new corporate website while ensuring it effectively tells our story. The revamped deck should focus on:

1. Visual Storytelling: Each slide should guide the audience through a clear and compelling narrative. Build on each slide to ensure the story flows seamlessly.

2. Minimal Text, More Visuals: Avoid text-heavy slides. Where text is necessary, keep it concise. Focus on strong visuals, icons, and imagery that reinforce key points. Ensure the visuals are impactful and align with our brand identity. Use bold icons and high-quality images that match the tone of the new website to emphasize key messages.

3. Design Consistency: Ensure the presentation reflects the color palette, typography, and imagery from the new website. This includes maintaining consistency in the style of headings, subheadings, and body text to reinforce our brand identity.

4. Modern & Clean Design: Embrace a minimalist design aesthetic inspired by the new website. Use the same color schemes, fonts, and clean layouts to ensure the slides are visually engaging and easy to digest.

5. Professional, Minimalist Look: Keep the design professional and minimalist, with a focus on clarity. Ensure each slide conveys its message clearly without unnecessary distractions.

Our goal is to create a visually engaging and interactive presentation that clearly communicates our message while keeping the audience engaged.

Ensure our corporate color scheme is maintained as per the current website: www.tovalinfo.net

Target Market(s)

B2B Clients in Asia Pacific and Australia

Industry/Entity Type

Across all industries, but more specific to IT

Requirements
Must have
• nsure our corporate color scheme is maintained as per the current website: www.tovalinfo.net
Nice to have
• More graphics and illustrations than text. Icon representations.
Should not have
• Slide Master SHOULD NOT include any specific contents. It should contain only essential elements such master layout, the logo, header, footer, and any repeating text elements and it should be limited to a maximum of 5 pages

```html
<!DOCTYPE html>
<html lang="en">
<head>
<meta charset="utf-8">
<title>TovalData Presentation Deck</title>
<link href="https://fonts.googleapis.com/css2?family=Nunito+Sans:wght@400;600;700;800&display=swap" rel="stylesheet">
<style>
:root{
  --red:#d32f2f;
  --red-deep:#b92424;
  --slate:#5b6781;
  --slate-dark:#4a5570;
  --ink:#3d4350;
  --body:#555b66;
  --paper:#f7f7f8;
  --canvas:#dfe2e6;
  --line:#c9cdd4;
  --white:#ffffff;
}
*{box-sizing:border-box;margin:0;padding:0}
html,body{width:1026px;height:1200px;overflow:hidden}
body{background:var(--canvas);font-family:"Nunito Sans",sans-serif;color:var(--ink);position:relative}
.slide{position:absolute;width:765px;height:430px;transform-origin:0 0;transform:scale(.5794);background:var(--paper);overflow:hidden;box-shadow:0 14px 30px rgba(60,70,90,.18)}
.col-l{left:51px}.col-r{left:531px}
.row-1{top:54px}.row-2{top:335px}.row-3{top:616px}.row-4{top:897px}
.top-band{position:absolute;left:0;top:0;width:765px;height:9px}
.title{position:absolute;left:42px;top:20px;font-size:23px;font-weight:600;color:var(--slate)}
.brand{position:absolute;right:44px;top:24px;display:flex;align-items:center;gap:5px;font-weight:800;font-size:17px;letter-spacing:2.5px;color:var(--slate)}
.brand-dot{width:7px;height:7px;background:var(--red)}
.footer{position:absolute;left:0;bottom:0;width:765px;height:26px;background:var(--slate);color:#e8ebf0;font-size:8px;display:flex;align-items:center;padding-left:42px}
.page-no{position:absolute;right:0;top:0;width:137px;height:26px;background:var(--red);color:#fff;font-weight:800;font-size:8.5px;letter-spacing:.6px;display:flex;align-items:center;justify-content:center}
.subhead{position:absolute;left:0;width:100%;text-align:center;font-size:16px;font-weight:600;color:var(--slate);line-height:1.35}
.lede{position:absolute;text-align:center;font-size:8.5px;color:var(--ink);line-height:1.6}
.icon-badge{position:absolute;width:48px;height:48px;border-radius:50%;display:flex;align-items:center;justify-content:center;box-shadow:0 3px 6px rgba(0,0,0,.18)}
.icon-badge.is-red{background:var(--red)}
.icon-badge.is-slate{background:var(--slate)}
.card{position:absolute;background:var(--white);border:1.5px solid var(--slate);border-radius:10px;box-shadow:0 4px 10px rgba(0,0,0,.08)}
.card.is-red{border-color:var(--red)}
.card-title{font-size:10.5px;font-weight:700;color:var(--ink);letter-spacing:.2px;line-height:1.35}
.card-tag{font-size:7.5px;font-weight:700;color:var(--red);line-height:1.45;margin-top:4px}
.card-body{font-size:7px;color:var(--body);line-height:1.7;margin-top:6px}

/* cover */
.cover{background:linear-gradient(135deg,#d83333 0%,#cf2b2b 55%,#c42626 100%)}
.cover .brand{left:44px;right:auto;top:22px;color:#fff}
.cover .brand-dot{background:#fff}
.cover-heading{position:absolute;left:42px;top:76px;width:300px;color:#fff;font-size:27px;font-weight:600;line-height:1.23}
.cover-pill{position:absolute;left:44px;top:257px;width:191px;height:34px;border:2px solid #fff;border-radius:17px;background:var(--slate);color:#fff;font-size:12px;font-weight:700;display:flex;align-items:center;justify-content:center}
.cover-art{position:absolute;left:380px;top:60px;width:320px;height:305px;border-radius:12px;background:radial-gradient(ellipse at 55% 45%,#f3f3f5 0%,#e9e3e4 35%,rgba(220,80,80,.0) 72%)}

/* solutions */
.hex-label{position:absolute;width:150px;text-align:center;font-size:9.5px;font-weight:700;color:var(--slate);line-height:1.5;letter-spacing:.2px}

/* usage */
.use-head{font-size:8px;font-weight:800;color:var(--ink);letter-spacing:.3px}
.use-text{font-size:7.5px;color:var(--body);line-height:1.6;margin-top:6px}
.use-block{position:absolute;width:160px}
.use-block.is-left{text-align:right;left:37px}
.use-block.is-right{left:566px;width:165px}
.hub-brand{position:absolute;left:317px;top:248px;width:130px;text-align:center;font-weight:800;font-size:13px;letter-spacing:2px;color:var(--slate)}

/* profiling */
.profile-box{position:absolute;width:176px;height:175px;border:1.5px dashed var(--slate)}
.profile-box.is-red{border-color:var(--red)}
.profile-inner{position:absolute;left:14px;top:14px;width:146px;height:146px;background:var(--slate);box-shadow:0 5px 10px rgba(0,0,0,.25);display:flex;flex-direction:column;align-items:center;justify-content:center;gap:14px;color:#fff;font-size:9.5px;font-weight:800;text-align:center;line-height:1.45}
.profile-box.is-red .profile-inner{background:var(--red)}
.profile-caption{position:absolute;width:176px;text-align:center;font-size:8.5px;color:var(--ink);line-height:1.6}
</style>
</head>
<body>

<!-- Slide 1: Cover -->
<section class="slide cover col-l row-1">
  <div class="brand">TOVALDATA<span class="brand-dot"></span></div>
  <h1 class="cover-heading">Data-Led, Content-Driven, Contact Center Empowered</h1>
  <div class="cover-pill">Integrated CX Solutions</div>
  <div class="cover-art" role="img" aria-label="Isometric illustration of a desktop monitor with cloud, analytics charts and floating data cubes"></div>
</section>

<!-- Slide 2: Four Core Pillars -->
<section class="slide col-r row-1">
  <svg class="top-band" viewBox="0 0 765 9"><rect x="0" y="5" width="765" height="4" fill="#e4e6ea"/><polygon points="0,0 525,0 515,9 0,9" fill="#d32f2f"/></svg>
  <h2 class="title">Our Four Core Pilers</h2>
  <div class="brand">TOVALDATA<span class="brand-dot"></span></div>

  <div class="card" style="left:44px;top:107px;width:151px;height:242px;padding:38px 13px 0">
    <div class="card-title">DATA</div>
    <div class="card-tag">Data-led Conversations With Potential Buyers</div>
    <div class="card-body">Data is at the heart of our expertise. We specialize in guiding you through the process of acquiring the precise data you need. Leveraging our proprietary dataset, along with our extensive Data Partner Network, we deliver tailored data solutions that align your marketing objectives.</div>
  </div>
  <div class="icon-badge is-slate" style="left:58px;top:82px"><svg width="24" height="24" viewBox="0 0 24 24"><circle cx="12" cy="12" r="7" fill="none" stroke="#fff" stroke-width="3" stroke-dasharray="3 2"/><circle cx="12" cy="12" r="3" fill="#fff"/></svg></div>

  <div class="card is-red" style="left:219px;top:107px;width:151px;height:242px;padding:38px 13px 0">
    <div class="card-title">REACHCX</div>
    <div class="card-tag">Harness The Power with AI Enhanced Content Channel</div>
    <div class="card-body">IT decision-makers rely on the latest industry insights and technology updates, keeping ReachCX's audience engaged and continuously expanding.<br>This loyal readership offers a prime marketing opportunity for technology companies seeking effective B2B lead generation</div>
  </div>
  <div class="icon-badge is-red" style="left:233px;top:82px"><svg width="24" height="24" viewBox="0 0 24 24"><rect x="6" y="6" width="12" height="12" rx="2" fill="none" stroke="#fff" stroke-width="2"/><path d="M9 2v4M15 2v4M9 18v4M15 18v4M2 9h4M2 15h4M18 9h4M18 15h4" stroke="#fff" stroke-width="1.6"/><text x="12" y="14.5" font-size="6" font-weight="800" fill="#fff" text-anchor="middle" font-family="Nunito Sans,sans-serif">AI</text></svg></div>

  <div class="card" style="left:395px;top:107px;width:151px;height:242px;padding:38px 13px 0">
    <div class="card-title">CONTACT CENTRE</div>
    <div class="card-tag">Driving Results Through Deep Customer Experience</div>
    <div class="card-body">Our hyper-localized contact centers are laser-focused on delivering exceptional customer experiences daily. With thousands of interactions with a diverse audience, we've developed a deep understanding of their daily challenges. We use these insights to drive better results for your business.</div>
  </div>
  <div class="icon-badge is-slate" style="left:409px;top:82px"><svg width="24" height="24" viewBox="0 0 24 24"><path d="M5 14v-3a7 7 0 0 1 14 0v3" fill="none" stroke="#fff" stroke-width="2"/><rect x="3" y="12" width="4" height="6" rx="1.5" fill="#fff"/><rect x="17" y="12" width="4" height="6" rx="1.5" fill="#fff"/><path d="M19 18q0 3-5 3" fill="none" stroke="#fff" stroke-width="1.6"/></svg></div>

  <div class="card is-red" style="left:571px;top:107px;width:151px;height:242px;padding:38px 13px 0">
    <div class="card-title">DIGITAL CHANNEL</div>
    <div class="card-tag">Precision Marketing Through Advanced Digital Channels.</div>
    <div class="card-body">Our sophisticated digital channel partnerships and technologies, combined with our experience, ensure that the right marketing messages reach the right audience at the right time</div>
  </div>
  <div class="icon-badge is-red" style="left:585px;top:82px"><svg width="24" height="24" viewBox="0 0 24 24"><path d="M10 21v-9a1.5 1.5 0 0 1 3 0v4h3a2 2 0 0 1 2 2v3" fill="none" stroke="#fff" stroke-width="2"/><path d="M7 9a5 5 0 0 1 9 0" fill="none" stroke="#fff" stroke-width="1.6"/></svg></div>

  <footer class="footer">©&nbsp; 2024 TovalData &nbsp;/&nbsp; All Rights Reserved<div class="page-no">PAGE NO 02</div></footer>
</section>

<!-- Slide 3: Our Solutions -->
<section class="slide col-l row-2">
  <svg class="top-band" viewBox="0 0 765 9"><rect x="0" y="5" width="765" height="4" fill="#e4e6ea"/><polygon points="0,0 525,0 515,9 0,9" fill="#d32f2f"/></svg>
  <h2 class="title">Our Solutions</h2>
  <div class="brand">TOVALDATA<span class="brand-dot"></span></div>

  <svg style="position:absolute;left:0;top:0" width="765" height="404" viewBox="0 0 765 404">
    <defs>
      <filter id="hexShadow" x="-20%" y="-20%" width="140%" height="140%"><feDropShadow dx="0" dy="4" stdDeviation="5" flood-color="#5b6781" flood-opacity=".18"/></filter>
      <polygon id="hex" points="0,-82 71,-41 71,41 0,82 -71,41 -71,-41" fill="#fff" stroke="#fff" stroke-width="12" stroke-linejoin="round"/>
    </defs>
    <g filter="url(#hexShadow)">
      <use href="#hex" x="128" y="200"/><use href="#hex" x="298" y="200"/><use href="#hex" x="467" y="200"/><use href="#hex" x="637" y="200"/>
      <use href="#hex" x="213" y="348"/><use href="#hex" x="383" y="348"/><use href="#hex" x="552" y="348"/>
    </g>
    <g fill="#d32f2f">
      <circle cx="128" cy="118" r="13"/><circle cx="128" cy="113" r="4.5" fill="#fff"/><path d="M120 126a8 6 0 0 1 16 0z" fill="#fff"/>
      <rect x="284" y="106" width="18" height="5" rx="1"/><rect x="284" y="113" width="18" height="5" rx="1"/><rect x="284" y="120" width="18" height="5" rx="1"/><circle cx="308" cy="118" r="7" fill="none" stroke="#d32f2f" stroke-width="3.5"/>
      <path d="M455 126l6-10 5 5 7-10 5 4v11z"/><rect x="458" y="108" width="3" height="6"/><rect x="466" y="104" width="3" height="6"/>
      <rect x="625" y="104" width="24" height="26" fill="none" stroke="#d32f2f" stroke-width="2"/><rect x="629" y="118" width="3" height="9"/><rect x="634" y="113" width="3" height="14"/><rect x="639" y="109" width="3" height="18"/><rect x="644" y="115" width="3" height="12"/>
      <rect x="200" y="254" width="24" height="22" rx="2" fill="none" stroke="#d32f2f" stroke-width="2.2"/><rect x="200" y="254" width="24" height="6"/><rect x="204" y="264" width="4" height="3"/><rect x="210" y="264" width="4" height="3"/><rect x="204" y="269" width="4" height="3"/><circle cx="224" cy="275" r="5"/>
      <circle cx="384" cy="257" r="6" fill="none" stroke="#d32f2f" stroke-width="2.5"/><rect x="382" y="264" width="4" height="5"/><path d="M371 280l8-6 8 3 6-4v10h-22z"/>
      <rect x="540" y="252" width="28" height="20" rx="2" fill="none" stroke="#d32f2f" stroke-width="2.2"/><rect x="545" y="262" width="3" height="6"/><rect x="550" y="258" width="3" height="10"/><circle cx="560" cy="262" r="4"/><rect x="550" y="274" width="8" height="4"/><rect x="544" y="278" width="20" height="2"/>
    </g>
  </svg>
  <div class="hex-label" style="left:53px;top:144px">ACCOUNT<br>PROFILING</div>
  <div class="hex-label" style="left:223px;top:144px">DATA<br>MANAGEMENT</div>
  <div class="hex-label" style="left:392px;top:144px">B2B CONTACT DATA<br>ACQUISITION</div>
  <div class="hex-label" style="left:562px;top:144px">EFFECTIVE<br>MULTI-CHANNEL<br>DEMAND GENERATION</div>
  <div class="hex-label" style="left:138px;top:292px">ATTENDEES<br>GENERATION<br>FOR EVENTS</div>
  <div class="hex-label" style="left:308px;top:292px">BUSINESS PROCESS<br>OUTSOURCING/CX<br>SOLUTIONS</div>
  <div class="hex-label" style="left:477px;top:292px">DIGITAL<br>MARKETING</div>

  <footer class="footer">©&nbsp; 2024 TovalData &nbsp;/&nbsp; All Rights Reserved<div class="page-no">PAGE NO 03</div></footer>
</section>

<!-- Slide 4: Master -->
<section class="slide col-r row-2">
  <svg class="top-band" viewBox="0 0 765 9"><rect x="0" y="5" width="765" height="4" fill="#e4e6ea"/><polygon points="0,0 525,0 515,9 0,9" fill="#d32f2f"/></svg>
  <h2 class="title">Master Slide</h2>
  <div class="brand">TOVALDATA<span class="brand-dot"></span></div>
  <footer class="footer">©&nbsp; 2024 TovalData &nbsp;/&nbsp; All Rights Reserved<div class="page-no">PAGE NO 04</div></footer>
</section>

<!-- Slide 5: Usage of Data -->
<section class="slide col-l row-3">
  <svg class="top-band" viewBox="0 0 765 9"><rect x="0" y="5" width="765" height="4" fill="#e4e6ea"/><polygon points="0,0 525,0 515,9 0,9" fill="#d32f2f"/></svg>
  <h2 class="title">Usage of Data</h2>
  <div class="brand">TOVALDATA<span class="brand-dot"></span></div>
  <div class="subhead" style="top:60px">InfoPlus data can be a functional asset for<br>organisation in the areas of:</div>

  <svg style="position:absolute;left:0;top:0" width="765" height="404" viewBox="0 0 765 404">
    <g stroke="#8a93a6" stroke-width="1" fill="none">
      <path d="M256 157H298L330 195"/><path d="M256 253H298"/><path d="M256 350H298L330 312"/>
      <path d="M509 157H467L435 195"/><path d="M509 253H467"/><path d="M509 350H467L435 312"/>
    </g>
    <circle cx="382" cy="255" r="76" fill="#fff" stroke="#5b6781" stroke-width="16"/>
    <g fill="#fff" stroke="#5b6781" stroke-width="1.5">
      <circle cx="330" cy="195" r="3"/><circle cx="298" cy="253" r="3"/><circle cx="330" cy="312" r="3"/>
      <circle cx="435" cy="195" r="3"/><circle cx="467" cy="253" r="3"/><circle cx="435" cy="312" r="3"/>
    </g>
    <g fill="#d32f2f">
      <circle cx="234" cy="157" r="21"/><circle cx="234" cy="253" r="21"/><circle cx="234" cy="350" r="21"/>
      <circle cx="531" cy="157" r="21"/><circle cx="531" cy="253" r="21"/><circle cx="531" cy="350" r="21"/>
    </g>
    <g fill="none" stroke="#fff" stroke-width="2">
      <circle cx="234" cy="157" r="7" stroke-dasharray="3 2"/><circle cx="234" cy="253" r="8"/><circle cx="234" cy="253" r="3"/>
      <path d="M234 358l-7-7a4 4 0 0 1 7-5 4 4 0 0 1 7 5z"/>
      <path d="M524 160l5-6 5 3 5-5M525 163h13"/><path d="M523 260h16M525 258v-4M529 258v-7M533 258v-5M537 258v-10"/>
      <circle cx="531" cy="350" r="8"/><path d="M531 342v8h8"/>
    </g>
  </svg>
  <div class="hub-brand">TOVALDATA</div>

  <div class="use-block is-left" style="top:122px"><div class="use-head">SALES</div><div class="use-text">Identify and plan new sales pipeline by building accurate prospect lists with validated contact to drive better sales leads.</div></div>
  <div class="use-block is-left" style="top:218px"><div class="use-head">MARKETING</div><div class="use-text">Create results-focused Account Based Marketing or field marketing campaigns with accurate contacts to maximise campaigns.</div></div>
  <div class="use-block is-left" style="top:315px"><div class="use-head">APPEND &amp; ENRICH</div><div class="use-text">Enriches existing database with accurate B2B data fields such as email address, company size, industry of targeted persona.</div></div>
  <div class="use-block is-right" style="top:122px"><div class="use-head">RECRUITING</div><div class="use-text">Get access to the top profiles of candidates and easily source the best talent, ensuring the most qualified candidates.</div></div>
  <div class="use-block is-right" style="top:218px"><div class="use-head">RESEARCH</div><div class="use-text">Quick and easy selections to populate, identify and build accurate APAC B2B data for different level of market research initiatives.</div></div>
  <div class="use-block is-right" style="top:315px"><div class="use-head">ANALYSIS</div><div class="use-text">Identify and plan new growth opportunities for untapped markets or new geographic areas by location, employees and much more.</div></div>

  <footer class="footer">©&nbsp; 2024 TovalData &nbsp;/&nbsp; All Rights Reserved<div class="page-no">PAGE NO 05</div></footer>
</section>

<!-- Slide 6: B2B Data Acquisition -->
<section class="slide col-r row-3">
  <svg class="top-band" viewBox="0 0 765 9"><rect x="0" y="5" width="765" height="4" fill="#e4e6ea"/><polygon points="0,0 525,0 515,9 0,9" fill="#d32f2f"/></svg>
  <h2 class="title">B2B Data Acquisition</h2>
  <div class="brand">TOVALDATA<span class="brand-dot"></span></div>
  <div class="subhead" style="top:60px">Power your growth and unleash the potential of Data</div>
  <p class="lede" style="left:44px;top:92px;width:677px">TovalData has extensive experience in managing customer and prospect data, which can significantly drive your growth. With our expertise in enhancing, connecting, profiling, and cleaning data, we can transform it into a powerful asset for your business. As data specialists, we excel in sourcing the most relevant data and applying it effectively to your campaigns.</p>

  <div class="card" style="left:58px;top:185px;width:203px;height:198px;padding:36px 18px 0">
    <div class="card-title">DATA ACCESS</div>
    <div class="card-body">Data is a core area of knowledge and expertise for us. We can effectively guide you through the process of purchasing the right data for your needs. Our own data set for is one of the most comprehensive in the market and can be obtained through a one-time purchase or an annual subscription.</div>
  </div>
  <div class="icon-badge is-slate" style="left:79px;top:160px"><svg width="24" height="24" viewBox="0 0 24 24"><rect x="3" y="5" width="18" height="5" rx="1" fill="none" stroke="#fff" stroke-width="1.6"/><rect x="3" y="13" width="18" height="5" rx="1" fill="none" stroke="#fff" stroke-width="1.6"/><circle cx="6" cy="7.5" r="1" fill="#fff"/><circle cx="6" cy="15.5" r="1" fill="#fff"/></svg></div>

  <div class="card is-red" style="left:281px;top:185px;width:204px;height:198px;padding:36px 18px 0">
    <div class="card-title">PLATFORM</div>
    <div class="card-body">InfoPlus is our enterprise business intelligence platform that provides access to high-quality, hard-to-reach B2B prospects. It features a comprehensive dataset with extensive filtering options, giving you ultimate control to target new markets and territories. With InfoPlus, you can expand your reach with a vast contacts database while maintaining complete control over your outreach efforts.</div>
  </div>
  <div class="icon-badge is-red" style="left:302px;top:160px"><svg width="24" height="24" viewBox="0 0 24 24"><rect x="4" y="6" width="16" height="13" rx="1" fill="none" stroke="#fff" stroke-width="1.8"/><circle cx="12" cy="12.5" r="3.5" fill="none" stroke="#fff" stroke-width="1.8" stroke-dasharray="2 1.4"/><path d="M8 2v3M12 2v3M16 2v3" stroke="#fff" stroke-width="1.4"/></svg></div>

  <div class="card" style="left:505px;top:185px;width:203px;height:198px;padding:36px 18px 0">
    <div class="card-title">CONCIERGE SERVICE</div>
    <div class="card-body">Connect with one of our data experts for a tailored consultation to receive a customized list of high-value contacts, specifically matched to your business needs.</div>
  </div>
  <div class="icon-badge is-slate" style="left:526px;top:160px"><svg width="24" height="24" viewBox="0 0 24 24"><circle cx="12" cy="12" r="7" fill="none" stroke="#fff" stroke-width="3.4" stroke-dasharray="3 2.5"/><circle cx="12" cy="12" r="2.5" fill="#fff"/></svg></div>

  <footer class="footer">©&nbsp; 2024 TovalData &nbsp;/&nbsp; All Rights Reserved<div class="page-no">PAGE NO 06</div></footer>
</section>

<!-- Slide 7: Data Expertise -->
<section class="slide col-l row-4">
  <svg class="top-band" viewBox="0 0 765 9"><rect x="0" y="5" width="765" height="4" fill="#e4e6ea"/><polygon points="0,0 525,0 515,9 0,9" fill="#d32f2f"/></svg>
  <h2 class="title">Harness the Power of Our Data Expertise</h2>
  <div class="brand">TOVALDATA<span class="brand-dot"></span></div>
  <div class="subhead" style="top:60px">We provide solutions to comprehensive Data Quality<br>Management Lifecycle.</div>
  <p class="lede" style="left:0;width:765px;top:105px">Partner with TovalData to add value to address your data quality challenges immediately.</p>

  <div class="card" style="left:57px;top:168px;width:150px;height:219px;padding:34px 12px 0">
    <div class="card-title">FUZZY<br>MATCHING</div>
    <div class="card-body">Quickly and accurately detect misspellings, abbreviations, and similar variations across diverse datasets using fuzzy matching. Build scalable, reusable configurations that support varying match types, including character-based and phonetic algorithms.</div>
  </div>
  <div class="icon-badge is-slate" style="left:72px;top:143px"><svg width="24" height="24" viewBox="0 0 24 24"><circle cx="12" cy="12" r="6" fill="none" stroke="#fff" stroke-width="3" stroke-dasharray="2.5 2"/><circle cx="12" cy="12" r="2" fill="#fff"/><path d="M19 4l2-2M3 21l2-2" stroke="#fff" stroke-width="1.6"/></svg></div>

  <div class="card is-red" style="left:224px;top:168px;width:151px;height:219px;padding:34px 12px 0">
    <div class="card-title">RECORD<br>LINKAGE</div>
    <div class="card-body">Are you dealing with fragmented data? Our record linkage software effortlessly merges multiple datasets, eliminating the need for manual matching or intricate coding. Enhance your data quality strategy with ease..</div>
  </div>
  <div class="icon-badge is-red" style="left:239px;top:143px"><svg width="24" height="24" viewBox="0 0 24 24"><path d="M3 7h7l2 2h9v11H3z" fill="#fff"/><rect x="7" y="3" width="12" height="5" fill="none" stroke="#fff" stroke-width="1.4"/></svg></div>

  <div class="card" style="left:392px;top:168px;width:150px;height:219px;padding:34px 12px 0">
    <div class="card-title">ADDRESS<br>VERIFICATION</div>
    <div class="card-body">Address validation ensures the accuracy and standardization of postal addresses by verifying correct spelling, formatting, abbreviations, and geocoding, as well as appending precise ZIP codes. This process is vital for ensuring successful deliveries, streamlined shipping, and targeted direct mail campaigns based on customer locations.</div>
  </div>
  <div class="icon-badge is-slate" style="left:407px;top:143px"><svg width="24" height="24" viewBox="0 0 24 24"><path d="M12 21s-6-6.5-6-11a6 6 0 0 1 12 0c0 4.5-6 11-6 11z" fill="none" stroke="#fff" stroke-width="2"/><circle cx="12" cy="10" r="2.3" fill="#fff"/></svg></div>

  <div class="card is-red" style="left:559px;top:168px;width:150px;height:219px;padding:34px 12px 0">
    <div class="card-title">DATA<br>DEDUPLICATION</div>
    <div class="card-body">Our data deduplication solution efficiently removes duplicate entries from your databases. Leveraging advanced data matching algorithms, it automatically identifies and eliminates identical records across systems, ensuring a unified and accurate source of truth.</div>
  </div>
  <div class="icon-badge is-red" style="left:574px;top:143px"><svg width="24" height="24" viewBox="0 0 24 24"><path d="M4 20h16" stroke="#fff" stroke-width="1.6"/><rect x="5" y="13" width="2.5" height="6" fill="#fff"/><rect x="9.5" y="10" width="2.5" height="9" fill="#fff"/><rect x="14" y="12" width="2.5" height="7" fill="#fff"/><rect x="18" y="8" width="2.5" height="11" fill="#fff"/><path d="M5 9l5-4 4 3 6-5" fill="none" stroke="#fff" stroke-width="1.5"/></svg></div>

  <footer class="footer">©&nbsp; 2024 TovalData &nbsp;/&nbsp; All Rights Reserved<div class="page-no">PAGE NO 07</div></footer>
</section>

<!-- Slide 8: Account Profiling -->
<section class="slide col-r row-4">
  <svg class="top-band" viewBox="0 0 765 9"><rect x="0" y="5" width="765" height="4" fill="#e4e6ea"/><polygon points="0,0 525,0 515,9 0,9" fill="#d32f2f"/></svg>
  <h2 class="title">Account Profiling</h2>
  <div class="brand">TOVALDATA<span class="brand-dot"></span></div>
  <div class="subhead" style="top:60px">Account Intelligence</div>
  <p class="lede" style="left:132px;width:500px;top:92px">Elevate your marketing efforts with precise account insights. Harness the power of our data intelligence and expertise to develop more effective strategies.</p>

  <div class="profile-box" style="left:84px;top:150px">
    <div class="profile-inner"><svg width="30" height="30" viewBox="0 0 30 30" fill="none" stroke="#fff" stroke-width="1.5"><circle cx="15" cy="9" r="4"/><circle cx="8" cy="12" r="3"/><circle cx="22" cy="12" r="3"/><path d="M5 24q4-8 10-8t10 8M3 20l5 5 4-3M27 20l-5 5-4-3"/></svg>DATA-LET INSIGHTS</div>
  </div>
  <div class="profile-box is-red" style="left:295px;top:150px">
    <div class="profile-inner"><svg width="30" height="30" viewBox="0 0 30 30" fill="none" stroke="#fff" stroke-width="1.5"><rect x="8" y="3" width="14" height="14"/><path d="M11 13l3-3 2 2 3-4"/><path d="M4 24l6-5 5 3 5-3 6 5"/></svg>INSIGHTFUL MARKET<br>ANALYSIS</div>
  </div>
  <div class="profile-box" style="left:506px;top:150px">
    <div class="profile-inner"><svg width="30" height="30" viewBox="0 0 30 30" fill="none" stroke="#fff" stroke-width="1.5"><rect x="4" y="6" width="12" height="20"/><path d="M7 11h6M7 15h6M7 19h6"/><circle cx="22" cy="10" r="3"/><path d="M17 22q0-6 5-6t5 6z"/></svg>INSTALLED AND<br>INTENT DATA</div>
  </div>
  <svg style="position:absolute;left:0;top:0" width="765" height="404" viewBox="0 0 765 404">
    <path d="M260 237H289" stroke="#5b6781" stroke-width="1.2"/><polygon points="295,237 288,233.5 288,240.5" fill="#5b6781"/>
    <path d="M471 237H500" stroke="#d32f2f" stroke-width="1.2"/><polygon points="506,237 499,233.5 499,240.5" fill="#d32f2f"/>
  </svg>
  <div class="profile-caption" style="left:84px;top:340px">Leverage our data intelligence to<br>build targeted accounts</div>
  <div class="profile-caption" style="left:295px;top:340px">Leverage our expertise and<br>infrastructure to conduct primary<br>and secondary research</div>
  <div class="profile-caption" style="left:506px;top:340px">Enhance with our Installed and<br>Intent signals to precisely build your<br>target account profiles</div>

  <footer class="footer">©&nbsp; 2024 TovalData &nbsp;/&nbsp; All Rights Reserved<div class="page-no">PAGE NO 08</div></footer>
</section>

</body>
</html>
```